Dietitian needs awesome business card

I need a contemporary design that's eye catching but professional.
My card is to given to doctors, specialists and patients alike.
I manage patients with chronic diseases
I have uploaded my logo and current business card, I would also like the other Certified Clinical Nutrition Adviser logo incorporated into the design

Target Market(s)

Doctors, specialists and patients

Industry/Entity Type

Healthcare

Contact Information for Business Card

www.brindlewaynutrition.com.au
Ph: 0427 514 903
Fax: 6482 7150
email: marcus.t.wellbeing@corvalmail.com
Space on the back of the card with: Appointment date, Appointment time and appointment location

Font styles to use
Serif

Colors
fbee3e
876aae
ffc214

Requirements
Must have
• My Logo
• Certified Clinical Nutrition Adviser Logo
• My 4 locations - Harrowfield Medical Centre, North Pellin Health, Kestwick Medical, Fernbrook Doctors Surgery
Nice to have
• I like the colours in my current business card

```html
<!DOCTYPE html>
<html lang="en">
<head>
<meta charset="utf-8">
<title>Brindleway Nutrition &amp; Dietetics – Business Card</title>
<link rel="stylesheet" href="https://fonts.googleapis.com/css2?family=Tinos:wght@400;700&family=Questrial&family=Quicksand:wght@700&family=Didact+Gothic&display=swap">
<style>
  :root {
    --bg: #e9e7e4;
    --card: #ffffff;
    --orange: #ff5a0a;
    --blue: #2b6fe6;
    --brand-blue: #1f46c9;
    --green: #8fe33c;
    --ink: #111111;
    --faint: #e8eaf8;
  }
  * { margin: 0; padding: 0; box-sizing: border-box; }
  html, body { width: 1200px; height: 1200px; overflow: hidden; background: var(--bg); }
  .canvas { position: relative; width: 1200px; height: 1200px; }

  .card { position: absolute; left: 151px; width: 898px; height: 519px; background: var(--card); overflow: hidden; box-shadow: 0 4px 14px rgba(0,0,0,.18); }
  .card--front { top: 82px; }
  .card--back { top: 621px; }
  .card__shapes { position: absolute; inset: 0; width: 100%; height: 100%; }

  .credential { position: absolute; left: 11px; top: 22px; width: 80px; color: #fff; font: 400 10px/13px "Questrial", sans-serif; }

  .brand { position: absolute; left: 230px; top: 60px; display: flex; align-items: center; gap: 18px; }
  .brand__dot { width: 128px; height: 128px; border-radius: 50%; background: var(--brand-blue); }
  .brand__name { color: var(--brand-blue); font-family: "Questrial", sans-serif; font-weight: 400; line-height: 1; }
  .brand__name .l1 { display: block; font-size: 56px; }
  .brand__name .l2 { display: block; font-size: 27px; margin-top: 6px; }

  .holder { position: absolute; left: 0; right: 0; top: 222px; text-align: center; padding-left: 0; width: 890px;
    font: 700 34px "Tinos", serif; color: var(--green); letter-spacing: .34em; }

  .contact { position: absolute; top: 338px; text-align: center; }
  .contact__label { font: 400 27px "Tinos", serif; color: var(--ink); }
  .contact__label b { font-weight: 700; }
  .contact__value { margin-top: 6px; font: 400 24px "Didact Gothic", sans-serif; color: var(--blue); letter-spacing: .02em; white-space: nowrap; }
  .contact--tel { left: 34px; width: 200px; }
  .contact--fax { left: 262px; width: 200px; }
  .contact--email { left: 470px; width: 400px; }
  .contact--email .contact__value { font-size: 20px; letter-spacing: 0; }

  .roles { position: absolute; left: 0; width: 894px; top: 470px; text-align: center; font: 700 27px "Quicksand", sans-serif; color: var(--green); letter-spacing: .08em; }
  .roles .sep { color: var(--blue); font-weight: 400; margin: 0 6px; }

  .back__title { position: absolute; left: 0; width: 898px; top: 26px; text-align: center; font: 400 54px "Questrial", sans-serif; color: var(--blue); letter-spacing: .08em; }
  .watermark { position: absolute; left: 28px; top: 230px; display: flex; align-items: center; gap: 40px; color: var(--faint); font-family: "Questrial", sans-serif; }
  .watermark__dot { width: 220px; height: 220px; border-radius: 50%; background: var(--faint); }
  .watermark__name { line-height: 1; }
  .watermark__name .l1 { display: block; font-size: 110px; }
  .watermark__name .l2 { display: block; font-size: 48px; margin-top: 8px; }

  .field { position: absolute; left: 66px; right: 60px; display: flex; align-items: flex-end; gap: 14px; }
  .field__label { font: 400 30px "Didact Gothic", sans-serif; color: var(--blue); line-height: 1; }
  .field__line { flex: 1; border-bottom: 1.5px solid var(--blue); margin-bottom: 2px; }
  .field--date { top: 120px; }
  .field--time { top: 250px; }
  .field--location { top: 380px; }
</style>
</head>
<body>
<main class="canvas">

  <section class="card card--front" aria-label="Business card front">
    <svg class="card__shapes" viewBox="0 0 898 519" aria-hidden="true">
      <path d="M0 0 H262 C150 60 40 160 0 258 Z" fill="var(--orange)"/>
      <circle cx="111" cy="42" r="27" fill="#ffffff"/>
      <path d="M876 0 H898 V519 H754 C860 480 900 420 880 330 C860 230 820 130 876 0 Z" fill="var(--blue)"/>
      <path d="M862 0 C808 130 846 230 866 330 C886 420 846 478 740 519 H754 C860 480 900 420 880 330 C860 230 820 130 876 0 Z" fill="var(--green)"/>
    </svg>
    <p class="credential">Certified Clinical Nutrition Adviser</p>

    <div class="brand">
      <span class="brand__dot"></span>
      <p class="brand__name"><span class="l1">Brindleway</span><span class="l2">Nutrition &amp; Dietetics</span></p>
    </div>

    <h1 class="holder">Marcus Thornbury</h1>

    <div class="contact contact--tel">
      <p class="contact__label">Tel<b>:</b></p>
      <p class="contact__value">0427 514 903</p>
    </div>
    <div class="contact contact--fax">
      <p class="contact__label">Fax<b>:</b></p>
      <p class="contact__value">6482 7150</p>
    </div>
    <div class="contact contact--email">
      <p class="contact__label">Email<b>:</b></p>
      <p class="contact__value">marcus.t.wellbeing@corvalmail.com</p>
    </div>

    <p class="roles">Dietitian<span class="sep">|</span>Nutritionist<span class="sep">|</span>Chef</p>
  </section>

  <section class="card card--back" aria-label="Business card back">
    <svg class="card__shapes" viewBox="0 0 898 519" aria-hidden="true">
      <rect x="0" y="0" width="898" height="8" fill="var(--green)"/>
      <rect x="0" y="512" width="898" height="7" fill="var(--blue)"/>
    </svg>
    <div class="watermark" aria-hidden="true">
      <span class="watermark__dot"></span>
      <p class="watermark__name"><span class="l1">Brindleway</span><span class="l2">Nutrition &amp; Dietetics</span></p>
    </div>
    <h2 class="back__title">APPOINTMENT</h2>
    <div class="field field--date"><span class="field__label">Date</span><span class="field__line"></span></div>
    <div class="field field--time"><span class="field__label">Time</span><span class="field__line"></span></div>
    <div class="field field--location"><span class="field__label">Location</span><span class="field__line"></span></div>
  </section>

</main>
</body>
</html>
```